The Quiet Hour Safeguard Handbook

A book cover. The book will be marketed as a promotional item for financial advisors, financial planners, independent insurance agents, bankers, and any professional who views their role as guardian of their clients assets and helping them manage risk.

```html
<!DOCTYPE html>
<html lang="en">
<head>
<meta charset="UTF-8">
<title>The Quiet Hour Safeguard Handbook — Book Cover</title>
<link rel="stylesheet" href="https://fonts.googleapis.com/css2?family=Bebas+Neue&family=Montserrat:ital,wght@0,500;1,300&display=swap">
<style>
  :root {
    --page-white: #ffffff;
    --cover-blue: #2d5479;
    --cover-blue-light: #3b6690;
    --accent-yellow: #e9c400;
    --text-white: #ffffff;
  }
  * { box-sizing: border-box; margin: 0; padding: 0; }
  html, body {
    width: 1200px;
    height: 1200px;
    overflow: hidden;
    background: var(--page-white);
  }
  .canvas {
    position: relative;
    width: 1200px;
    height: 1200px;
  }
  .cover {
    position: absolute;
    left: 191px;
    top: 81px;
    width: 818px;
    height: 1038px;
    background: var(--cover-blue);
    overflow: hidden;
  }
  .circuit-texture {
    position: absolute;
    inset: 0;
    background:
      radial-gradient(ellipse 60% 45% at 50% 58%, rgba(90, 130, 175, 0.35), rgba(45, 84, 121, 0) 70%),
      var(--cover-blue);
  }
  .top-rule {
    position: absolute;
    left: 0;
    top: 40px;
    width: 100%;
    height: 3px;
    background: var(--accent-yellow);
  }
  .title {
    position: absolute;
    left: 0;
    width: 100%;
    text-align: center;
    font-family: "Bebas Neue", "Oswald", sans-serif;
    line-height: 1;
  }
  .title-lead {
    top: 86px;
    font-size: 84px;
    color: var(--text-white);
  }
  .title-main {
    top: 146px;
    font-size: 200px;
    color: var(--accent-yellow);
    letter-spacing: 1px;
  }
  .title-sub {
    top: 328px;
    font-size: 86px;
    color: var(--text-white);
    letter-spacing: 1px;
  }
  .divider {
    position: absolute;
    left: 252px;
    width: 314px;
    height: 12px;
  }
  .divider-top { top: 519px; }
  .divider-bottom { top: 649px; }
  .subtitle {
    position: absolute;
    left: 0;
    top: 543px;
    width: 100%;
    text-align: center;
    font-family: "Montserrat", sans-serif;
    font-style: italic;
    font-weight: 300;
    font-size: 37px;
    line-height: 49px;
    color: var(--accent-yellow);
  }
  .tagline {
    position: absolute;
    left: 0;
    top: 828px;
    width: 100%;
    text-align: center;
    font-family: "Montserrat", sans-serif;
    font-weight: 500;
    font-size: 23px;
    line-height: 31px;
    letter-spacing: 2.5px;
    color: var(--text-white);
  }
  .author {
    position: absolute;
    left: 0;
    top: 941px;
    width: 100%;
    text-align: center;
    font-family: "Montserrat", sans-serif;
    font-weight: 500;
    font-size: 34px;
    letter-spacing: 2px;
    color: var(--text-white);
  }
</style>
</head>
<body>
<div class="canvas">
  <section class="cover">
    <div class="circuit-texture" role="img" aria-label="Faint circuit-board pattern of traces and nodes across the blue cover"></div>
    <div class="top-rule"></div>

    <h1>
      <span class="title title-lead">The</span>
      <span class="title title-main">Quiet Hour</span>
      <span class="title title-sub">Safeguard Handbook</span>
    </h1>

    <svg class="divider divider-top" viewBox="0 0 314 12" aria-hidden="true">
      <line x1="0" y1="6" x2="146" y2="6" stroke="#e9c400" stroke-width="1.5"/>
      <polygon points="157,1 162,6 157,11 152,6" fill="#e9c400"/>
      <line x1="168" y1="6" x2="314" y2="6" stroke="#e9c400" stroke-width="1.5"/>
    </svg>

    <p class="subtitle">Protect Yourself and<br>Your Family in the AI Age</p>

    <svg class="divider divider-bottom" viewBox="0 0 314 12" aria-hidden="true">
      <line x1="0" y1="6" x2="146" y2="6" stroke="#e9c400" stroke-width="1.5"/>
      <polygon points="157,1 162,6 157,11 152,6" fill="#e9c400"/>
      <line x1="168" y1="6" x2="314" y2="6" stroke="#e9c400" stroke-width="1.5"/>
    </svg>

    <p class="tagline">IT’S BETTER TO HAVE IT AND NOT NEED IT<br>THAN NED IT AND NOT HAVE IT.</p>

    <p class="author">AUTHOR NAME</p>
  </section>
</div>
</body>
</html>
```